Premium men's gut health supplement needs a bottle label designed

We’re velnora - a premium men’s wellness brand focused on gut health. Our first product is a high-quality daily supplement designed to support digestion, regularity, and internal cleanliness. Backed by science and tailored for modern lifestyles, velnora is crafted in the UK and proudly LGBT-owned. It aims to resolve intimacy problems that gay men may experience due to poor digestion but also does not exclude any other orientation - other men may use it simply to improve their digestion.

velnora is for health-conscious men who value science-backed supplements and want to feel confident from the inside out. Many of our early adopters will be gay and bisexual men who prioritise gut health as part of their self-care, sexual, and hygiene routine, though the product is equally effective and appealing to anyone seeking premium digestive support.

The product is premium the target customer is male, not specific to one location but primary markets will be US, UK and EU.

I’d like a supplement bottle designed for velnora, our premium men’s gut health brand. The focus should be clean, slightly clinical, and minimal - inspired by brands like Quelrin and Darvo. The key element is the wordmark (velnora) on the front, with no additional logo or icon. Lowercase text and a strong, contemporary font are preferred.

The bottle should be aesthetically pleasing so that people are proud to display it on their shelf, instead of hiding it in a cupboard (like Quelrin, darvo, Pia Venturek, Morvanel etc)

Avoid anything that shows the product as being for LGBT, e.g., no rainbows, men holding hands etc.

The design should be premium, minimalist and not be busy or overwhelming.

I have uploaded a file called "Bottle" to give an idea of the type of container, but please ignore the colours and change as you see fit. This is just for reference for the type of bottle we'll use - all colours are customisable.

I have also uploaded some images for "style" reference, e.g., darvo, quelrin, pia venturek, etc for inspiration.

```html
<!DOCTYPE html>
<html lang="en">
<head>
<meta charset="utf-8">
<title>velnora — daily gut health supplement label</title>
<link rel="stylesheet" href="https://fonts.googleapis.com/css2?family=Lexend:wght@400;500;600&display=swap">
<style>
  :root {
    --backdrop: #f2f2f2;
    --label-light: #d0c9c7;
    --label-dark: #c2bab8;
    --ink: #2b2828;
    --gold: #c9a23a;
    --tab: #2e2d2d;
    --tab-text: #e6e2df;
  }
  * { box-sizing: border-box; margin: 0; padding: 0; }
  html, body {
    width: 730px;
    height: 1200px;
    overflow: hidden;
    background: var(--backdrop);
  }
  .canvas {
    position: relative;
    width: 730px;
    height: 1200px;
  }
  .label {
    position: absolute;
    left: 0;
    top: 108px;
    width: 730px;
    height: 984px;
    background: linear-gradient(90deg, var(--label-light) 0%, var(--label-dark) 100%);
    color: var(--ink);
    font-family: "Lexend", sans-serif;
    overflow: hidden;
  }
  .label__trim {
    position: absolute;
    left: 0; top: 0;
    width: 100%;
    height: 3px;
    background: var(--gold);
  }
  .wordmark {
    position: absolute;
    left: 66px;
    top: 206px;
    width: 96px;
    height: 480px;
    writing-mode: vertical-rl;
    transform: rotate(180deg);
    font-family: "Lexend", sans-serif;
    font-weight: 600;
    font-size: 96px;
    line-height: 96px;
    letter-spacing: 0;
    text-align: center;
    color: var(--ink);
    white-space: nowrap;
  }
  .claims {
    position: absolute;
    left: 186px;
    top: 206px;
  }
  .claims__headline {
    font-size: 18px;
    font-weight: 500;
    line-height: 24px;
    white-space: nowrap;
  }
  .claims__box {
    display: inline-block;
    margin-top: 10px;
    padding: 5px 10px;
    border: 2px solid var(--ink);
    font-size: 13.5px;
    font-weight: 500;
    line-height: 17px;
    white-space: nowrap;
  }
  .claims__box--wide { width: 411px; }
  .claims__box--narrow { width: 300px; margin-top: 12px; }
  .claims__tagline {
    margin-top: 14px;
    font-size: 18px;
    font-weight: 500;
    line-height: 24px;
  }
  .tier-tab {
    position: absolute;
    right: 0;
    top: 346px;
    width: 60px;
    height: 190px;
    background: var(--tab);
    display: flex;
    align-items: center;
    justify-content: center;
  }
  .tier-tab__text {
    transform: rotate(-90deg);
    color: var(--tab-text);
    font-size: 22px;
    font-weight: 500;
    white-space: nowrap;
  }
  .origin {
    position: absolute;
    left: 58px;
    top: 876px;
  }
  .origin__place {
    font-size: 14.5px;
    font-weight: 500;
    line-height: 20px;
  }
  .origin__proof {
    font-size: 20px;
    font-weight: 500;
    line-height: 26px;
  }
</style>
</head>
<body>
<main class="canvas">
  <section class="label">
    <div class="label__trim"></div>
    <h1 class="wordmark">velnora</h1>
    <div class="claims">
      <p class="claims__headline">Science + technology for modern gut care</p>
      <p class="claims__box claims__box--wide">Supports digestion, regularity &amp; internal cleansing.</p><br>
      <p class="claims__box claims__box--narrow">Daily gut health supplement for men</p>
      <p class="claims__tagline">Where science meets self-care</p>
    </div>
    <div class="tier-tab"><span class="tier-tab__text">premium</span></div>
    <div class="origin">
      <p class="origin__place">Made in the UK ·</p>
      <p class="origin__proof">Backed by science</p>
    </div>
  </section>
</main>
</body>
</html>
```